Dancing Beyond Dawn Book Cover

We are looking for a book cover that will capture the audience who are GEN X and Boomer Women looking to change their life. We need the book cover to be in alignment with our Brand DancingBeyondDawn.example

Target Market(s)

women 45+

Font styles to use
Other font styles liked:
• Montserrat

Colors
EE7325
F08F49
F5BC92
FAE3D3
FDF4ED
EB3D1F
EC4F4E
F09395
F8D3D4
FCEDEE
E54698
E96AAD
F1A4CE
F9D9EA
FCEFF6

Requirements
Must have
• FUN
Should not have
• too cutsey!

```html
<!DOCTYPE html>
<html lang="en">
<head>
<meta charset="utf-8">
<title>Dancing Beyond Dawn – Book Cover</title>
<link href="https://fonts.googleapis.com/css2?family=Montserrat:wght@200;300;400;500&display=swap" rel="stylesheet">
<style>
  :root {
    --backdrop: #fe706f;
    --paper: #ffffff;
    --ink: #111111;
    --coral: #fe6f6d;
    --coral-soft: #f8837e;
    --rose: #f09395;
    --blush: #f9c4b9;
  }
  * { margin: 0; padding: 0; box-sizing: border-box; }
  html, body {
    width: 1200px; height: 1000px; overflow: hidden;
    background: var(--backdrop);
    font-family: "Montserrat", sans-serif;
  }
  .book-cover {
    position: absolute; left: 343px; top: 113px;
    width: 524px; height: 768px;
    background: var(--paper);
  }
  .brand-mark {
    position: absolute; right: 28px; top: 46px;
    display: flex; align-items: center; gap: 6px;
    font-size: 10px; font-weight: 500; color: var(--coral);
    letter-spacing: 0.04em;
  }
  .brand-dot {
    width: 14px; height: 14px; border-radius: 50%;
    background: var(--coral);
  }
  .author-heart {
    position: absolute; left: 45px; top: 91px;
    width: 420px; height: 367px;
  }
  .title {
    position: absolute; left: 0; right: 0; top: 478px;
    text-align: center; color: var(--ink); line-height: 1;
    text-transform: uppercase; font-weight: 200;
  }
  .title-line { display: block; }
  .title-top { font-size: 76px; font-weight: 200; letter-spacing: 0.01em; }
  .title-mid { font-size: 44px; font-weight: 200; letter-spacing: 0.03em; margin-top: 2px; }
  .title-bottom { font-size: 96px; font-weight: 400; letter-spacing: 0.01em; margin-top: -6px; }
  .subtitle {
    position: absolute; left: 0; right: 0; top: 698px;
    text-align: center; font-size: 11.5px; font-weight: 500;
    letter-spacing: 0.07em; color: var(--ink); text-transform: uppercase;
  }
</style>
</head>
<body>
  <main class="book-cover">
    <div class="brand-mark"><span class="brand-dot"></span>Dancing Beyond Dawn</div>

    <svg class="author-heart" viewBox="-12 -12 444 388" role="img" aria-label="Photo of the two smiling authors inside a heart frame">
      <defs>
        <linearGradient id="author-photo" x1="0" y1="0" x2="0" y2="1">
          <stop offset="0" stop-color="var(--coral)"/>
          <stop offset="0.6" stop-color="var(--coral-soft)"/>
          <stop offset="1" stop-color="var(--rose)"/>
        </linearGradient>
      </defs>
      <path d="M210 44 C180 8 130 0 95 0 C40 0 0 45 0 110 C0 200 120 300 210 362 C300 300 420 200 420 110 C420 45 380 0 325 0 C290 0 240 8 210 44 Z"
            fill="url(#author-photo)" stroke="var(--blush)" stroke-width="16" stroke-linejoin="round"/>
    </svg>

    <h1 class="title">
      <span class="title-line title-top">Dancing</span>
      <span class="title-line title-mid">Beyond</span>
      <span class="title-line title-bottom">Dawn</span>
    </h1>
    <p class="subtitle">A woman's guide to living it up without the booze</p>
  </main>
</body>
</html>
```